Torlen Caribbean BANK Website Design with UX/UI

I need a website DEV Design Mock up that can be presented in full HTML. Not code needed...just clickable design.
This is a BANk website.
We wil send some websites we like a bit later.
We need at least 10 pages that are Full HTML and integrated.
I will send more Design requirement details.
but feel free to go for it and be ahead

Hi
This is a Bank.
It will be based in the Caribbean. Please read up a bit about the Caribbean so you appreciate our region.
Therefore the only ethnicity that can be used is African American. Go to pixelmarta and search African American People so you can see the ethnicity of the people whom you must feature

The colour Scheme will be those of the Logo. The pantones were provided but it is the BLUE and Yellowish Orange

Target Market(s)

All Bank Customers

Industry/Entity Type

Banking

Number of Pages Required

5+ page

Colors
6b449b
ffc214

Requirements
Must have
• Logo
Follow the Brand Architecture
Use the Pantones provided
Follow the Suite Map Provided
Follow the brief Attached

```html
<!DOCTYPE html>
<html lang="en">
<head>
<meta charset="utf-8">
<title>Torlen Caribbean BANK – Car Loan</title>
<link href="https://fonts.googleapis.com/css2?family=Roboto:wght@400;500;700&display=swap" rel="stylesheet">
<style>
:root{
  --purple:#5f2a9c;
  --purple-dark:#4a1f80;
  --yellow:#f8d000;
  --white:#ffffff;
  --grey:#6b6b6b;
  --ink:#3a3a3a;
}
*{margin:0;padding:0;box-sizing:border-box}
html,body{width:1200px;height:4580px;overflow:hidden}
body{font-family:'Roboto',Arial,sans-serif;background:var(--white);position:relative;color:var(--ink)}
.section{position:absolute;left:0;width:1200px}
a{color:inherit}

/* ticker */
.ticker{top:0;height:53px;background:var(--purple);display:flex;align-items:center;white-space:nowrap;overflow:hidden;font-size:13px;font-weight:500;color:var(--yellow)}
.ticker span{text-decoration:underline;margin-right:28px}
.ticker i{font-style:normal;margin-right:28px;color:var(--yellow)}

/* header */
.header{top:53px;height:112px;background:var(--white)}
.brand{position:absolute;left:96px;top:30px;display:flex;align-items:center;gap:10px;color:var(--purple);font-weight:700;font-size:17px;line-height:1.1;width:150px}
.brand-dot{width:26px;height:26px;border-radius:50%;background:var(--yellow);flex:none}
.main-nav{position:absolute;left:298px;top:44px;display:flex;align-items:center;font-size:15px;font-weight:700;color:var(--purple)}
.main-nav a{text-decoration:none;padding:7px 6px}
.main-nav .sep{margin:0 4px}
.main-nav .active{background:var(--purple);color:var(--white)}
.search{position:absolute;left:1014px;top:50px;width:126px;border-bottom:2px solid var(--purple);font-size:14px;font-style:italic;color:var(--purple);padding-bottom:4px;display:flex;justify-content:space-between}

/* sub nav */
.subnav{top:165px;height:59px;background:var(--purple);display:flex;align-items:center;justify-content:center;font-size:14px;font-weight:500;color:var(--white)}
.subnav a{text-decoration:none;padding:6px 6px}
.subnav .sep{margin:0 6px}
.subnav .active{background:var(--white);color:var(--purple)}
.strip{background:var(--yellow)}

/* photos */
.photo{position:absolute;inset:0}
.hero-photo{background:linear-gradient(120deg,#dcd6d4 0%,#8a7f86 45%,#3d4a6b 75%,#d8dfe6 100%)}
.wheel-photo{background:linear-gradient(110deg,#5d3a9a 0%,#4b2a86 40%,#6c48a6 70%,#5a3696 100%)}
.keys-photo{background:linear-gradient(100deg,#6e6e70 0%,#9a9ba0 30%,#3b3f4a 60%,#a8a9ae 100%)}
.money-photo{background:linear-gradient(180deg,#6b3fb0 0%,#7a52b6 55%,#8b6cba 100%)}

.card{position:absolute;background:var(--purple);color:var(--white);padding:70px 24px 0 34px}
.card h2{font-size:44px;font-weight:500}
.rule{width:96px;height:4px;background:var(--yellow);margin:24px 0 26px}
.card p{font-size:17px;font-weight:500;line-height:1.45}
.btn{display:inline-block;background:var(--yellow);color:var(--purple);font-size:18px;font-weight:500;text-decoration:none;padding:15px 34px}
.card .btn{margin-top:26px}

.whatsnew{top:900px;height:76px;background:var(--yellow);overflow:hidden}
.whatsnew .label{position:absolute;left:0;top:0;height:76px;width:200px;background:var(--purple);color:var(--white);font-size:25px;font-weight:500;display:flex;align-items:center;padding-left:36px;clip-path:polygon(0 0,180px 0,200px 50%,180px 100%,0 100%)}
.whatsnew .items{position:absolute;left:210px;top:28px;white-space:nowrap;font-size:13px;font-weight:500;color:var(--purple)}
.whatsnew .items span{text-decoration:underline;margin-right:28px}
.whatsnew .items i{font-style:normal;margin-right:28px}

.center-copy{position:absolute;left:0;width:1200px;text-align:center;color:var(--white)}
.center-copy h2{font-size:44px;font-weight:500}
.center-copy .rule{margin:24px auto 32px}
.center-copy p{font-size:17px;font-weight:500;line-height:1.45;width:600px;margin:0 auto 26px}

/* contact */
.contact{top:3431px;height:564px}
.contact-col{position:absolute;top:175px;width:380px}
.contact-col h3{display:flex;align-items:center;gap:18px;font-size:45px;font-weight:500;color:var(--purple)}
.contact-col p{margin-top:22px;font-size:17px;line-height:1.4;color:var(--grey)}
.contact-col .detail{margin-top:24px;font-size:20px;font-weight:500;color:var(--purple);line-height:1.6;width:460px}

.loanbar{top:3995px;height:87px;background:var(--yellow);display:flex;align-items:center;justify-content:center;font-size:21px;font-weight:500;color:var(--purple)}
.loanbar a{text-decoration:underline}
.loanbar .sep{margin:0 20px}

.footer{top:4082px;height:434px}
.foot-col{position:absolute;top:80px}
.foot-col h4{font-size:19px;font-weight:700;color:var(--ink);display:inline-block;padding-bottom:10px;border-bottom:3px solid var(--purple);width:170px}
.foot-col ul{list-style:none;margin-top:16px}
.foot-col li{font-size:17px;font-weight:500;color:var(--grey);line-height:34px}
.foot-col li::before{content:"•";margin-right:14px}

.copyright{top:4516px;height:64px;background:var(--purple);color:var(--white);display:flex;align-items:center;justify-content:space-between;padding:0 90px 0 44px;font-size:21px;font-weight:500}
.legal{color:#cdb5ff;font-size:19px}
.legal a{text-decoration:underline}
.legal .sep{margin:0 12px}
</style>
</head>
<body>

<div class="section ticker">
  <i>|</i><span>COVID - 19 MEASURES HAVE BEEN TAKEN FOR ALL BANKING FEATURES.</span><i>|</i><span>COVID - 19 MEASURES HAVE BEEN TAKEN FOR ALL BANKING FEATURES.</span><i>|</i><span>COVID - 19 MEASURES HAVE BEEN TAKEN FOR ALL BANKING FEATURES.</span>
</div>

<header class="section header">
  <div class="brand"><span class="brand-dot"></span>Torlen Caribbean BANK</div>
  <nav class="main-nav">
    <a>CHECKING</a><span class="sep">|</span><a>SAVINGS</a><span class="sep">|</span><a class="active">CREDIT CARDS</a><span class="sep">|</span><a class="active">CAR LOANS</a><span class="sep">|</span><a class="active">MORTGAGES</a><span class="sep">|</span><a>INVESTMENTS</a>
  </nav>
  <div class="search"><span>Search....</span>
    <svg width="16" height="16" viewBox="0 0 16 16"><circle cx="6.5" cy="6.5" r="4.5" fill="none" stroke="#5f2a9c" stroke-width="2"/><line x1="10" y1="10" x2="14" y2="14" stroke="#5f2a9c" stroke-width="2.5"/></svg>
  </div>
</header>

<nav class="section subnav">
  <a>PERSONAL</a><span class="sep">|</span><a class="active">SMALL BUSINESS</a><span class="sep">|</span><a>PRIVATE BANKING</a><span class="sep">|</span><a>CORPORATE</a><span class="sep">|</span><a>WEALTH</a><span class="sep">|</span><a>ONLINE BANKING</a><span class="sep">|</span><a>ATM &amp; BRANCH</a><span class="sep">|</span><a>HELP &amp; SUPPORT</a><span class="sep">|</span><a>CAREERS</a>
</nav>
<div class="section strip" style="top:224px;height:18px"></div>

<section class="section" style="top:242px;height:658px">
  <div class="photo hero-photo" role="img" aria-label="Smiling family standing beside a new blue car at a dealership"></div>
  <div class="card" style="left:0;top:71px;width:363px;height:466px">
    <h2>Car Loan</h2>
    <div class="rule"></div>
    <p>Lorem Ipsum is simply dummy text of the printing and typesetting industry. Lorem Ipsum has been the industry's standard dummy text ever since the 1500s.</p>
    <a class="btn">Apply Now</a>
  </div>
</section>

<div class="section whatsnew">
  <div class="label">What's New</div>
  <div class="items"><span>ANKING FEATURES.</span><i>|</i><span>COVID - 19 MEASURES HAVE BEEN TAKEN FOR ALL BANKING FEATURES.</span><i>|</i><span>COVID - 19 MEASURES HAVE BEEN TAKEN</span></div>
</div>

<section class="section" style="top:976px;height:791px">
  <div class="photo wheel-photo" role="img" aria-label="Driver's hands on a steering wheel inside a car, purple tint"></div>
  <div class="center-copy" style="top:245px">
    <h2>Get your Wheels of Independence...</h2>
    <div class="rule"></div>
    <p>Lorem Ipsum is simply dummy text of the printing and typesetting industry. Lorem Ipsum has been the industry's standard dummy text ever since the 1500s.</p>
    <a class="btn">Apply Now</a>
  </div>
</section>
<div class="section strip" style="top:1767px;height:77px"></div>

<section class="section" style="top:1844px;height:810px">
  <div class="photo keys-photo" role="img" aria-label="Car keys being handed over into an open palm"></div>
  <div class="card" style="left:837px;top:135px;width:363px;height:465px">
    <h2>Dummy Text</h2>
    <div class="rule"></div>
    <p>Lorem Ipsum is simply dummy text of the printing and typesetting industry. Lorem Ipsum has been the industry's standard dummy text ever since the 1500s.</p>
    <a class="btn">Apply Now</a>
  </div>
</section>
<div class="section strip" style="top:2654px;height:77px"></div>

<section class="section" style="top:2731px;height:700px">
  <div class="photo money-photo" role="img" aria-label="Toy car beside stacks of coins and a small figure, purple tint"></div>
  <div class="center-copy" style="top:162px">
    <h2>100% Financing with up to 7 years to pay!</h2>
    <div class="rule"></div>
    <p>Lorem Ipsum is simply dummy text of the printing and typesetting industry. Lorem Ipsum has been the industry's standard dummy text ever since the 1500s.</p>
    <a class="btn">Apply Now</a>
  </div>
</section>

<section class="section contact">
  <div class="contact-col" style="left:128px">
    <h3><svg width="36" height="36" viewBox="0 0 36 36"><circle cx="18" cy="18" r="18" fill="#5f2a9c"/><path d="M12 10c1-1 2.5-1 3 0l1.5 3c.4.8 0 1.6-.6 2l-1 .8c.8 2 2.4 3.6 4.4 4.4l.8-1c.5-.6 1.3-1 2-.6l3 1.5c1 .5 1 2 0 3-2 2-4.5 2-8-1s-6-6.5-6-9c0-1.2.4-2.2.9-3.1z" fill="#fff"/></svg>Call Us</h3>
    <p>Lorem Ipsum is simply dummy text of the printing and typesetting industry. Lorem Ipsum has been the industry's standard dummy text ever since the 1500s.</p>
    <div class="detail">Phone - 9999-9999<br>Email - dummy@mail.com</div>
  </div>
  <div class="contact-col" style="left:645px;width:460px">
    <h3><svg width="36" height="36" viewBox="0 0 36 36"><circle cx="18" cy="18" r="18" fill="#5f2a9c"/><circle cx="18" cy="15" r="6" fill="none" stroke="#fff" stroke-width="2"/><path d="M10 27c2-4 5-5 8-5s6 1 8 5" fill="none" stroke="#fff" stroke-width="2"/></svg>Arrange a Callback</h3>
    <p style="width:380px">Lorem Ipsum is simply dummy text of the printing and typesetting industry. Lorem Ipsum has been the industry's standard dummy text ever since the 1500s.</p>
    <div class="detail">Arrange a Callback</div>
  </div>
</section>

<nav class="section loanbar">
  <a>MORTGAGE LOAN</a><span class="sep">|</span><a>CAR LOAN</a><span class="sep">|</span><a>PERSONAL LOAN</a><span class="sep">|</span><a>RENOVATIONS LOAN</a><span class="sep">|</span><a>BUSINESS LOAN</a>
</nav>

<footer class="section footer">
  <div class="foot-col" style="left:92px"><h4>QUICK LINKS</h4><ul><li>OUR STORY</li><li>INVESTOR RELATIONS</li><li>SECURITY CENTER</li><li>CUSTOMER SERVICE</li><li>NEWSROOM</li></ul></div>
  <div class="foot-col" style="left:393px"><h4>SERVICES</h4><ul><li>INVESTMENT SERVICES</li><li>INSURANCE SERVICES</li><li>WEALTH SOLUTIONS</li><li>REMOTE BANKING</li><li>STUDENT BANKING</li><li>RENOVATION LAN</li><li>CAR LOAN</li></ul></div>
  <div class="foot-col" style="left:681px"><h4>LOANS</h4><ul><li>MORGAGE LOAN</li><li>CAR LOAN</li><li>PERSONAL LOAN</li><li>RENOVATION LOAN</li><li>BUSINESS LOAN</li></ul></div>
  <div class="foot-col" style="left:926px"><h4>IMPORTANT LINKS</h4><ul><li>CONTACT US</li><li>PRIVACY</li><li>MORTGAGES</li><li>SITEMAP</li></ul></div>
</footer>

<div class="section copyright">
  <span>Copyright Torlen | All Rights Reserved</span>
  <span class="legal"><a>PRIVACY</a><span class="sep">|</span><a>MORGAGES</a><span class="sep">|</span><a>CONTACT US</a><span class="sep">|</span><a>SITEMAP</a></span>
</div>

</body>
</html>
```